DELVANE ROOFING YARD SIGN

We need a yard sign to put in our customers' yards when we are roofing their home.
Delvane Roofing
468 Pettigrew Rd
Lake Charles LA 70452
phone: 337-555-0148

Maybe some verbiage like "Your Hometown Roofing Experts"
or
"Family Owned Since 1956"

```html
<!DOCTYPE html>
<html lang="en">
<head>
<meta charset="utf-8">
<title>Delvane Roofing Yard Sign</title>
<link rel="stylesheet" href="https://fonts.googleapis.com/css2?family=Libre+Caslon+Text:wght@700&family=Urbanist:wght@500;600&display=swap">
<style>
  :root {
    --ink: #0e0e0e;
    --paper: #ffffff;
    --backdrop: #eceeef;
    --panel-light: #e3e3e5;
    --silver-dark: #9c9c9c;
    --silver-mid: #cfcfcf;
    --silver-bright: #f6f6f6;
    --roof-dark: #151515;
    --roof-light: #8a8a8a;
    --ring: #9a9a9a;
  }
  html, body {
    margin: 0;
    width: 1200px;
    height: 1200px;
    overflow: hidden;
    background: var(--backdrop);
  }
  .yard-sign {
    position: absolute;
    left: 40px;
    top: 181px;
    width: 1120px;
    height: 838px;
    box-shadow: 0 6px 24px rgba(0,0,0,0.12);
  }
  .yard-sign svg { display: block; width: 100%; height: 100%; }
  .brand-title {
    font-family: "Libre Caslon Text", Georgia, serif;
    font-weight: 700;
    font-size: 128px;
    fill: var(--ink);
  }
  .tagline {
    font-family: "Urbanist", Arial, sans-serif;
    font-weight: 600;
    font-size: 64px;
    fill: var(--paper);
  }
  .address {
    font-family: "Urbanist", Arial, sans-serif;
    font-weight: 500;
    font-size: 38px;
    fill: var(--paper);
  }
  .heritage {
    font-family: "Urbanist", Arial, sans-serif;
    font-weight: 600;
    font-size: 38px;
    fill: var(--ink);
  }
  .heritage-year {
    font-family: "Libre Caslon Text", Georgia, serif;
    font-weight: 700;
    font-size: 88px;
    fill: var(--ink);
  }
  .emblem-name {
    font-family: "Urbanist", Arial, sans-serif;
    font-weight: 600;
    font-size: 32px;
    fill: var(--ink);
  }
  .phone-number {
    font-family: "Libre Caslon Text", Georgia, serif;
    font-weight: 700;
    font-size: 118px;
    fill: var(--ink);
  }
</style>
</head>
<body>
<div class="yard-sign">
  <svg viewBox="0 0 1316 985" xmlns="http://www.w3.org/2000/svg">
    <defs>
      <linearGradient id="silver-sheen" x1="0" y1="0" x2="1" y2="0">
        <stop offset="0" stop-color="var(--silver-dark)"/>
        <stop offset="0.5" stop-color="var(--silver-bright)"/>
        <stop offset="1" stop-color="var(--silver-mid)"/>
      </linearGradient>
      <linearGradient id="roof-tone" x1="0" y1="0" x2="1" y2="1">
        <stop offset="0" stop-color="var(--roof-dark)"/>
        <stop offset="0.5" stop-color="var(--roof-light)"/>
        <stop offset="1" stop-color="var(--roof-dark)"/>
      </linearGradient>
    </defs>

    <rect class="sign-base" x="0" y="0" width="1316" height="985" fill="var(--paper)"/>

    <text class="brand-title" x="658" y="162" text-anchor="middle" textLength="1140" lengthAdjust="spacingAndGlyphs">DELVANE ROOFING</text>

    <g class="tagline-band">
      <polygon points="0,198 667,198 737,490 0,490" fill="var(--ink)"/>
      <text class="tagline" x="80" y="316">Your Hometown</text>
      <text class="tagline" x="80" y="387">Roofing Experts</text>
      <rect x="80" y="418" width="196" height="6" fill="var(--paper)"/>
      <polygon class="roof-photo" role="img" aria-label="Close-up photo of dark roof tiles in diagonal rows" points="682,198 1316,198 1316,490 752,490" fill="url(#roof-tone)"/>
    </g>

    <g class="info-row">
      <polygon points="0,505 372,505 487,777 0,777" fill="var(--ink)"/>
      <path class="pin-icon" transform="translate(76,546) scale(1.9)" fill="var(--paper)" d="M12 2C8.1 2 5 5.1 5 9c0 5.2 7 13 7 13s7-7.8 7-13c0-3.9-3.1-7-7-7zm0 9.5a2.5 2.5 0 1 1 0-5 2.5 2.5 0 0 1 0 5z"/>
      <text class="address" x="130" y="580">468 Pettigrew</text>
      <text class="address" x="130" y="629">Rd Lake</text>
      <text class="address" x="130" y="678">Charles LA</text>
      <text class="address" x="130" y="727">70452</text>

      <polygon points="389,505 837,505 952,777 504,777" fill="url(#silver-sheen)"/>
      <text class="heritage" x="644" y="580" text-anchor="middle">Family Owned</text>
      <text class="heritage" x="655" y="631" text-anchor="middle">Since</text>
      <text class="heritage-year" x="660" y="722" text-anchor="middle">1956</text>

      <polygon points="852,505 1316,505 1316,777 967,777" fill="var(--panel-light)"/>
      <circle class="emblem-ring" cx="1107" cy="640" r="124" fill="var(--paper)" stroke="var(--ring)" stroke-width="3"/>
      <text class="emblem-name" x="1107" y="632" text-anchor="middle">Delvane</text>
      <text class="emblem-name" x="1107" y="670" text-anchor="middle">Roofing</text>
    </g>

    <g class="phone-line">
      <g class="phone-icon" transform="translate(236,812) scale(4)" fill="var(--ink)">
        <path d="M6.6 10.8c1.4 2.8 3.8 5.1 6.6 6.6l2.2-2.2c.3-.3.7-.4 1-.2 1.1.4 2.3.6 3.6.6.6 0 1 .4 1 1V20c0 .6-.4 1-1 1C10.6 21 3 13.4 3 4c0-.6.4-1 1-1h3.5c.6 0 1 .4 1 1 0 1.3.2 2.5.6 3.6.1.3 0 .7-.2 1L6.6 10.8z"/>
        <path d="M14 3.2a7 7 0 0 1 6.8 6.8" fill="none" stroke="var(--ink)" stroke-width="1.6" stroke-linecap="round"/>
        <path d="M13.6 6.6a3.6 3.6 0 0 1 3.8 3.8" fill="none" stroke="var(--ink)" stroke-width="1.6" stroke-linecap="round"/>
      </g>
      <text class="phone-number" x="368" y="904" textLength="710" lengthAdjust="spacingAndGlyphs">337-555-0148</text>
    </g>
  </svg>
</div>
</body>
</html>
```